The Larkspur Bay Clinic Flyer Design

The Larkspur Bay Clinic is a new company providing Dietetic services for people with gastrointestinal disorders. The main client base would be people suffering from Irritable Bowel Syndrome. IBS is a collection of symptoms which (will be individual to the suffer) including constipation/diarrhoea/abdominal pain or discomfort/bloating/belching/flatulence/stomach gurgling/reflux/nausea/urgency/incomplete emptying/fatigue/headaches. IBS affects approx 30% of the population. Previous treatments have generally been ineffectual and include medication, hypnotherapy, healthy eating.
Recently it has been found that the FODMAP diet (a diet low in fermentable Carbohydrates) has been effective in 75% of sufferers.
The Low FODMAP diet is complex and it is highly recommended that it is undertaken only under the supervision of a suitably qualified dietitian. Treatment is available within the QWR but is usually accessible only following consultation with a Gastroenterologist. Most GP's have never heard of this treatment as the research was only published in 2009 in Australia and is yet to filter through to the general practitioner. The Larkspur Bay Clinic is the only clinic in the UK offering dietetic lead specialist services.
I am a member of the KSL and RWMT (logos provided)
The flyer would be double sided, informing the patient of all the self help steps they could take if they have IBS then recommending that they contact The Larkspur Bay Clinic for specialist advice.
Self Help: Healthy eating, regular meals, good intake of non caffeinated non alcoholic non fizzy drinks, regular exercise, stress management.
The flyer would be left in GP surgeries, Health centres, holistic therapy centres, or through doors.
Majority female aged 20-50, able to pay for private services
Clinic

```html
<!DOCTYPE html>
<html lang="en">
<head>
<meta charset="utf-8">
<title>The Larkspur Bay Clinic – Flyer</title>
<link rel="stylesheet" href="https://fonts.googleapis.com/css2?family=Open+Sans:wght@400;600;700;800&display=swap">
<style>
  :root {
    --backdrop: #c9c9cb;
    --paper: #ffffff;
    --teal: #2a8a9b;
    --sky: #1fa6dd;
    --sky-light: #bfe6f7;
    --olive: #b9b84a;
    --navy: #1f4a7a;
    --red: #e3262b;
    --ink: #1c1c1c;
  }
  * { box-sizing: border-box; margin: 0; padding: 0; }
  html, body { width: 1200px; height: 860px; overflow: hidden; }
  body {
    background: var(--backdrop);
    font-family: "Open Sans", Arial, sans-serif;
    color: var(--ink);
    position: relative;
  }
  .flyer {
    position: absolute;
    width: 536px;
    height: 754px;
    background: var(--paper);
    overflow: hidden;
    box-shadow: 4px 5px 8px rgba(0,0,0,0.25);
  }
  .flyer--front { left: 59px; top: 41px; }
  .flyer--back { left: 622px; top: 65px; }

  .photo { position: absolute; }
  .stripe { position: absolute; background: var(--olive); }

  .brand {
    position: absolute;
    display: flex; align-items: center; gap: 10px;
    background: var(--paper);
    color: var(--ink); font-weight: 400; font-size: 22px; line-height: 1.1;
  }
  .brand__square { width: 16px; height: 16px; background: var(--ink); flex: none; }

  .band {
    position: absolute; left: 0; bottom: 0; width: 100%;
    background: var(--teal); color: #fff;
  }
  .band b { font-weight: 700; }

  /* ---------- front ---------- */
  .front__hero {
    left: 0; top: 0; width: 536px; height: 260px;
    background: radial-gradient(ellipse at 46% 48%, #e0584f 0%, #d88780 26%, #9a9a9a 58%, #d9d9d9 100%);
  }
  .front__wave { position: absolute; left: 0; top: 130px; width: 536px; height: 240px; }
  .social-tag {
    position: absolute; left: 14px; top: 12px;
    display: flex; align-items: center; gap: 6px;
    background: var(--navy); color: #fff;
    padding: 5px 9px; font-size: 11px; font-weight: 700; line-height: 1.1;
  }
  .social-tag__square { width: 14px; height: 14px; background: #fff; }
  .headline {
    position: absolute; left: 304px; top: 214px;
    font-weight: 700; letter-spacing: 2.5px; color: var(--ink); line-height: 1;
  }
  .headline__top { font-size: 29px; display: block; }
  .headline__bottom { font-size: 20px; display: block; margin-top: 6px; }
  .headline__gut { color: var(--red); font-size: 40px; letter-spacing: 3px; }

  .front .stripe--left { left: 0; top: 281px; width: 16px; height: 355px; }
  .front .stripe--right { right: 0; top: 396px; width: 17px; height: 240px; }

  .symptoms { position: absolute; left: 32px; top: 293px; }
  .symptoms__title {
    color: var(--navy); font-weight: 700; font-size: 17.5px;
    line-height: 1.3; letter-spacing: 0.8px;
  }
  .symptoms__list { list-style: none; margin-top: 14px; margin-left: 16px; }
  .symptoms__list li {
    font-size: 13px; line-height: 20px; letter-spacing: 1px;
    position: relative; padding-left: 12px;
  }
  .symptoms__list li::before {
    content: ""; position: absolute; left: 0; top: 9px;
    width: 3px; height: 3px; background: var(--olive);
  }
  .front__figure {
    left: 318px; top: 330px; width: 120px; height: 280px;
    background: linear-gradient(180deg, #e8c4a8 0%, #e2b99d 45%, #f2eeea 70%, #ddb495 100%);
    border-radius: 40px 40px 10px 10px;
  }
  .front .band { height: 118px; display: flex; align-items: flex-end; justify-content: center; padding-bottom: 28px; font-size: 13px; }
  .front__fruit {
    left: 16px; top: 569px; width: 286px; height: 127px;
    background: linear-gradient(120deg, #c33a2a 0%, #e7892a 30%, #6a8f2c 55%, #7b2e4e 80%, #d8a33a 100%);
  }
  .front .brand { left: 302px; top: 618px; width: 216px; height: 78px; padding-left: 10px; }

  /* ---------- back ---------- */
  .back__topline { position: absolute; left: 0; top: 0; width: 100%; height: 16px; background: linear-gradient(90deg, var(--sky-light), var(--sky)); }
  .back__hero {
    left: 0; top: 16px; width: 536px; height: 356px;
    background: linear-gradient(180deg, #dfeccb 0%, #b8d88a 45%, #7fb446 75%, #5f9a30 100%);
  }
  .back .brand {
    left: 293px; top: 55px; width: 220px; height: 70px;
    border: 1px solid var(--olive); padding: 0 12px;
  }
  .back .band { height: 115px; display: flex; align-items: flex-end; justify-content: center; padding-bottom: 26px; font-size: 15px; }
  .back__card { position: absolute; left: 15px; top: 372px; width: 503px; height: 323px; background: var(--paper); }
  .back .stripe--left { left: 0; top: 372px; width: 15px; height: 323px; }

  .offer { position: absolute; left: 32px; top: 383px; width: 480px; }
  .offer__title { color: var(--red); font-weight: 700; font-size: 17.5px; line-height: 1.35; }
  .offer__body { margin-top: 14px; font-size: 13px; line-height: 18px; }

  .self-help { position: absolute; left: 26px; top: 560px; }
  .self-help__title { color: var(--navy); font-weight: 800; font-size: 24px; letter-spacing: 1.5px; line-height: 1.2; }
  .self-help__list { list-style: none; margin-top: 2px; }
  .self-help__list li { font-size: 16px; line-height: 25px; }
  .self-help__num { color: var(--olive); font-weight: 700; margin-right: 4px; }
  .back__produce {
    left: 232px; top: 534px; width: 132px; height: 144px; border-radius: 8px;
    background: linear-gradient(135deg, #d9503a 0%, #f0a03a 45%, #7aa83a 100%);
  }
  .badge { position: absolute; }
  .badge--register { left: 446px; top: 560px; width: 69px; height: 56px; background: var(--navy); }
  .badge--association { left: 378px; top: 641px; width: 137px; height: 44px; background: #9fc8ea; }
</style>
</head>
<body>

<section class="flyer flyer--front front">
  <div class="photo front__hero" role="img" aria-label="Photo of hands resting on a stomach with a red glow showing pain"></div>
  <div class="social-tag"><span class="social-tag__square"></span><span>Find us on<br>Chatterly</span></div>

  <svg class="front__wave" viewBox="0 0 536 240" preserveAspectRatio="none" aria-hidden="true">
    <defs>
      <linearGradient id="waveFill" x1="0" y1="0" x2="1" y2="0">
        <stop offset="0" stop-color="#e4f4fc"/>
        <stop offset="0.45" stop-color="#7fd0f0"/>
        <stop offset="1" stop-color="#1a9fdc"/>
      </linearGradient>
    </defs>
    <path d="M0 110 C90 70 170 60 250 62 C350 64 450 40 536 0 L536 240 L0 240 Z" fill="url(#waveFill)"/>
    <path d="M0 150 C70 115 170 95 250 100 C330 105 380 170 440 200 C480 218 510 226 536 230 L536 240 L0 240 Z" fill="#ffffff"/>
  </svg>

  <h1 class="headline">
    <span class="headline__top">What's your</span>
    <span class="headline__bottom"><span class="headline__gut">GUT</span> feeling?</span>
  </h1>

  <div class="stripe stripe--left"></div>
  <div class="stripe stripe--right"></div>

  <div class="symptoms">
    <h2 class="symptoms__title">DO YOU HAVE<br>THE SYMPTOMS?</h2>
    <ul class="symptoms__list">
      <li>constipation</li>
      <li>diarrhoea</li>
      <li>constipation</li>
      <li>abdominal pain</li>
      <li>abdominal discomfort</li>
      <li>urgency to open your bowels</li>
      <li>mucus, flatulence</li>
      <li>wind, belching, burping, nausea</li>
      <li>vomiting, reflux, indigestion,</li>
      <li>fatigue, tired</li>
    </ul>
  </div>

  <div class="photo front__figure" role="img" aria-label="Photo of a slim waist holding a bunch of green leaves"></div>

  <footer class="band"><span><b>The Larkspur Bay Clinic</b> - 14 Marlow Lane Bristol BS9 7QT</span></footer>

  <div class="photo front__fruit" role="img" aria-label="Photo of an assortment of fresh fruit"></div>
  <div class="brand"><span class="brand__square"></span><span>The Larkspur<br>Bay Clinic</span></div>
</section>

<section class="flyer flyer--back back">
  <div class="back__topline"></div>
  <div class="photo back__hero" role="img" aria-label="Photo of a smiling young woman lying on grass holding an apple beside a bowl of fruit"></div>

  <div class="brand"><span class="brand__square"></span><span>The Larkspur<br>Bay Clinic</span></div>

  <footer class="band"><span>Contact <b>The Larkspur Bay Clinic</b> for specialist advice: <b>07700900418</b></span></footer>
  <div class="back__card"></div>
  <div class="stripe stripe--left"></div>

  <div class="offer">
    <h2 class="offer__title">You do not have to PUT UP with the symptoms<br>there is a NEW solution!</h2>
    <p class="offer__body">
      Dietary treatment with the <b>FODMAP</b> diet is clinically proven to work<br>
      in up to 75% of patients.<br>
      Results can be seen usually within 1-2 weeks.<br>
      Treatment involves 1 x 1 hr teaching session on the elimination phase.
    </p>
  </div>

  <div class="self-help">
    <h3 class="self-help__title">SELF HELP:</h3>
    <ol class="self-help__list">
      <li><span class="self-help__num">1.</span>Healthy eating</li>
      <li><span class="self-help__num">2.</span>Regular exercise</li>
      <li><span class="self-help__num">3.</span>Stress management</li>
    </ol>
  </div>

  <div class="photo back__produce" role="img" aria-label="Illustration of fresh fruit and vegetables arranged together"></div>

  <div class="badge badge--register" aria-hidden="true"></div>
  <div class="badge badge--association" aria-hidden="true"></div>
</section>

</body>
</html>
```